Gestaltung eines Bieretiketts gesucht
Zielgruppe
Wir sind eine Numetal Band und möchten an unsere Freunde,Fans und Weggefährten ein kleines individuelles Give Away in Form von Bier abgeben. Dazu benötigen wir ein Bieretikette.
+++Aufgrund eines kurzfristig Auslandsaufenthalt, kann keine Bewertung der Designvorschläge bis zum Ende der Laufzeit abgegeben werden. Am Samstag, 06.02.16 erfolgt die Ermittlung des Gewinndesigns. Sorry & Danke für das Verständnis.+++
Aufgabenstellung
Als Give Away möchten wir Bierflaschen mit einem individuellen Etiketten-Design verteilen. Wir stellen uns das Etikett wie die bekannten Bieretiketten vor. Die Vorderseite des Designs könnte einen Gerstenkranz, ein Hopfenbild oder einen Lorbeerkranz aufzeigen. Wir könnten uns aber auch vorstellen, dass nur der Name quer, waagerecht oder senkrecht dargestellt wird. Der Fantasie sind keine Grenzen gesetzt.
Die Rückseite wäre mit folgenden Infos zu versehen:
www.rustyfoxmoon.example
Wieselquellbräu, Merligen, Schweiz
0,33l
Alc. 4.5% Vol
Hals: Ein kleines Etikette
Die Schrift wäre: Impact
Anhang:
Darin enthalten die Schriftart, sowie die Farbkennung. Der Logoschriftzug muss nicht zwingend grün sein, sondern kann auch weiss od. schwarz sein.
Wenn Verwendung dafür können diese Utensilien gerne verwendet werden
Hierbei handelt es sich um das runde Bandlogo.
Dies soll unsere benötigen Etiketten darstellen (Vorne, hinten, Hals).
Gerne stehen wir für weitere Fragen zur Verfügung.

```html
<!DOCTYPE html>
<html lang="de">
<head>
<meta charset="utf-8">
<title>Rusty Fox Moon – Bieretikett</title>
<link rel="stylesheet" href="https://fonts.googleapis.com/css2?family=Alfa+Slab+One&family=Anton&display=swap">
<style>
  :root {
    --label-black: #1d1d1b;
    --brand-green: #2a9b3a;
    --ink-white: #ffffff;
    --page-white: #ffffff;
    --art-grey: #8a8a88;
  }
  html, body {
    margin: 0;
    padding: 0;
    width: 1200px;
    height: 3759px;
    overflow: hidden;
    background: var(--page-white);
  }
  .canvas {
    position: relative;
    width: 1200px;
    height: 3759px;
  }
  .neck-label {
    position: absolute;
    left: 315px;
    top: 115px;
    width: 571px;
    height: 284px;
    background: var(--label-black);
    display: flex;
    align-items: center;
    justify-content: center;
  }
  .neck-mark {
    display: flex;
    align-items: center;
    gap: 18px;
  }
  .neck-mark__circle {
    width: 70px;
    height: 70px;
    border-radius: 50%;
    background: var(--brand-green);
  }
  .neck-mark__name {
    font-family: "Anton", "Impact", sans-serif;
    font-size: 84px;
    line-height: 1;
    color: var(--brand-green);
    letter-spacing: 2px;
  }
  .front-label {
    position: absolute;
    left: 314px;
    top: 477px;
    width: 572px;
    height: 646px;
    background: var(--label-black);
    overflow: hidden;
  }
  .front-label__title {
    position: absolute;
    left: 0;
    right: 0;
    top: 28px;
    margin: 0;
    text-align: center;
    font-family: "Alfa Slab One", "Impact", serif;
    font-weight: 400;
    color: var(--brand-green);
    text-transform: uppercase;
    line-height: 1;
  }
  .front-label__title span { display: block; }
  .front-label__title .line-1 { font-size: 66px; letter-spacing: 2px; }
  .front-label__title .line-2 { font-size: 84px; letter-spacing: 4px; }
  .boombox-art {
    position: absolute;
    left: 24px;
    top: 202px;
    width: 524px;
    height: 270px;
    background: linear-gradient(180deg, #d9d9d7 0%, var(--art-grey) 55%, #4a4a48 100%);
    opacity: 0.85;
  }
  .badge-shape {
    position: absolute;
    left: 278px;
    top: 330px;
    width: 250px;
    height: 130px;
    background: var(--label-black);
    border: 7px solid var(--ink-white);
    transform: rotate(-20deg);
  }
  .front-label__variety {
    position: absolute;
    left: 0;
    right: 0;
    top: 488px;
    margin: 0;
    text-align: center;
    font-family: "Alfa Slab One", "Impact", serif;
    font-weight: 400;
    font-size: 76px;
    letter-spacing: 3px;
    line-height: 1;
    color: var(--brand-green);
  }
  .front-label__facts {
    position: absolute;
    left: 36px;
    right: 40px;
    top: 574px;
    display: flex;
    justify-content: space-between;
    font-family: "Anton", "Impact", sans-serif;
    font-size: 42px;
    line-height: 1;
    color: var(--ink-white);
  }
</style>
</head>
<body>
<main class="canvas">
  <section class="neck-label" aria-label="Halsetikett">
    <div class="neck-mark">
      <span class="neck-mark__circle" aria-hidden="true"></span>
      <span class="neck-mark__name">KVT</span>
    </div>
  </section>

  <section class="front-label" aria-label="Vorderetikett">
    <h1 class="front-label__title">
      <span class="line-1">Rusty Fox</span>
      <span class="line-2">Moon</span>
    </h1>
    <div class="boombox-art" role="img" aria-label="Grafik eines Ghettoblasters in Weiß und Grau"></div>
    <div class="badge-shape" aria-hidden="true"></div>
    <h2 class="front-label__variety">KRACHER</h2>
    <div class="front-label__facts">
      <span class="facts__abv">Alc. 4.5% Vol</span>
      <span class="facts__volume">0,33l</span>
    </div>
  </section>
</main>
</body>
</html>
```